Unique Editable Recipe Cards

Create 10 unique editable recipe cards. Please look at Quonly and see what Editable Recipe cards are popular to get an idea of what Cards will sell. Search for "Editable Recipe Cards". The final images will need to be editable in Canva.

```html
<!DOCTYPE html>
<html lang="en">
<head>
<meta charset="utf-8">
<title>Editable Recipe Cards</title>
<link rel="stylesheet" href="https://fonts.googleapis.com/css2?family=Almendra:wght@400;700&family=Barlow:wght@400;500&display=swap">
<style>
  :root {
    --backdrop: #767676;
    --card: #ffffff;
    --ink: #1f1f1f;
    --rule: #2a2a2a;
    --cookie-title: #d98d35;
    --cookie-heading: #6b3a2e;
    --berry-title: #c8202f;
    --berry-heading: #2f4a25;
  }
  * { box-sizing: border-box; margin: 0; padding: 0; }
  html, body { width: 1200px; height: 1200px; overflow: hidden; background: var(--backdrop); }
  .recipe-card {
    position: absolute; left: 249px; width: 702px; height: 502px;
    background: var(--card); overflow: hidden;
    box-shadow: 0 3px 6px rgba(0,0,0,.25);
  }
  .recipe-card--cookie { top: 79px; }
  .recipe-card--berry { top: 619px; }
  .photo { position: absolute; }
  .cookie-photo {
    left: 0; top: 0; width: 198px; height: 502px;
    background: linear-gradient(160deg, #c98a45 0%, #ffffff 22%, #5a3426 38%, #ffffff 55%, #c98a45 70%, #dcdcdc 88%, #c98a45 100%);
    opacity: .85;
    -webkit-mask-image: linear-gradient(90deg, #000 70%, transparent 100%);
            mask-image: linear-gradient(90deg, #000 70%, transparent 100%);
  }
  .berry-photo-corner {
    left: 494px; top: 0; width: 208px; height: 211px;
    background: radial-gradient(circle at 60% 45%, #d2334a 0%, #3f6b3a 55%, rgba(255,255,255,0) 78%);
  }
  .berry-photo-border {
    left: 0; top: 437px; width: 356px; height: 65px;
    background: linear-gradient(180deg, rgba(255,255,255,0) 0%, #d2334a 55%, #3f6b3a 100%);
    -webkit-mask-image: linear-gradient(90deg, #000 80%, transparent 100%);
            mask-image: linear-gradient(90deg, #000 80%, transparent 100%);
  }
  .card-title {
    position: absolute; font-family: 'Almendra', serif; font-weight: 700;
    font-size: 70px; line-height: 1; letter-spacing: 1px;
  }
  .recipe-card--cookie .card-title { left: 246px; top: 14px; color: var(--cookie-title); }
  .recipe-card--berry .card-title { left: 261px; top: 26px; color: var(--berry-title); }
  .field-label {
    position: absolute; font-family: 'Barlow', sans-serif; font-size: 16px;
    line-height: 16px; color: var(--ink); white-space: nowrap;
  }
  .section-heading {
    position: absolute; font-family: 'Almendra', serif; font-size: 26px;
    line-height: 1; letter-spacing: 1.5px;
  }
  .recipe-card--cookie .section-heading { color: var(--cookie-heading); top: 198px; }
  .recipe-card--berry .section-heading { color: var(--berry-heading); top: 211px; }
  .rule { position: absolute; height: 1.3px; background: var(--rule); }
</style>
</head>
<body>

<section class="recipe-card recipe-card--cookie">
  <div class="photo cookie-photo" role="img" aria-label="Chocolate chip cookies, a bowl of chocolate chips and measuring spoons"></div>
  <h1 class="card-title">Recipe</h1>

  <span class="field-label" style="left:246px;top:102px">RECIPE NAME:</span>
  <div class="rule" style="left:365px;top:117px;width:303px"></div>
  <span class="field-label" style="left:246px;top:123px">FROM THE KITCHEN OF:</span>
  <div class="rule" style="left:434px;top:138px;width:234px"></div>
  <span class="field-label" style="left:246px;top:145px">SERVES:</span>
  <div class="rule" style="left:313px;top:160px;width:56px"></div>
  <span class="field-label" style="left:373px;top:145px">PREP TIME:</span>
  <div class="rule" style="left:459px;top:160px;width:35px"></div>
  <span class="field-label" style="left:502px;top:145px">COOK TIME:</span>
  <div class="rule" style="left:591px;top:160px;width:77px"></div>

  <h2 class="section-heading" style="left:189px">Ingredients</h2>
  <h2 class="section-heading" style="left:429px">Directions</h2>

  <div class="rule" style="left:188px;top:250px;width:215px"></div>
  <div class="rule" style="left:188px;top:273px;width:215px"></div>
  <div class="rule" style="left:188px;top:296px;width:215px"></div>
  <div class="rule" style="left:188px;top:319px;width:215px"></div>
  <div class="rule" style="left:188px;top:342px;width:215px"></div>
  <div class="rule" style="left:188px;top:364px;width:215px"></div>
  <div class="rule" style="left:188px;top:387px;width:215px"></div>
  <div class="rule" style="left:188px;top:409px;width:215px"></div>
  <div class="rule" style="left:188px;top:431px;width:215px"></div>
  <div class="rule" style="left:188px;top:453px;width:215px"></div>

  <div class="rule" style="left:429px;top:250px;width:242px"></div>
  <div class="rule" style="left:429px;top:273px;width:242px"></div>
  <div class="rule" style="left:429px;top:296px;width:242px"></div>
  <div class="rule" style="left:429px;top:319px;width:242px"></div>
  <div class="rule" style="left:429px;top:342px;width:242px"></div>
  <div class="rule" style="left:429px;top:364px;width:242px"></div>
  <div class="rule" style="left:429px;top:387px;width:242px"></div>
  <div class="rule" style="left:429px;top:409px;width:242px"></div>
  <div class="rule" style="left:429px;top:431px;width:242px"></div>
  <div class="rule" style="left:429px;top:453px;width:242px"></div>
</section>

<section class="recipe-card recipe-card--berry">
  <div class="photo berry-photo-corner" role="img" aria-label="Sprig of red hypericum berries with green leaves"></div>
  <div class="photo berry-photo-border" role="img" aria-label="Row of red berry sprigs along the bottom edge"></div>
  <h1 class="card-title">Recipe</h1>

  <span class="field-label" style="left:32px;top:117px">RECIPE NAME:</span>
  <div class="rule" style="left:150px;top:132px;width:335px"></div>
  <span class="field-label" style="left:32px;top:139px">FROM THE KITCHEN OF:</span>
  <div class="rule" style="left:221px;top:153px;width:264px"></div>
  <span class="field-label" style="left:32px;top:161px">SERVES:</span>
  <div class="rule" style="left:99px;top:175px;width:56px"></div>
  <span class="field-label" style="left:159px;top:161px">PREP TIME:</span>
  <div class="rule" style="left:247px;top:175px;width:34px"></div>
  <span class="field-label" style="left:286px;top:161px">COOK TIME:</span>
  <div class="rule" style="left:378px;top:175px;width:107px"></div>

  <h2 class="section-heading" style="left:34px">Ingredients</h2>
  <h2 class="section-heading" style="left:352px">Directions</h2>

  <div class="rule" style="left:32px;top:260px;width:285px"></div>
  <div class="rule" style="left:32px;top:283px;width:285px"></div>
  <div class="rule" style="left:32px;top:306px;width:285px"></div>
  <div class="rule" style="left:32px;top:329px;width:285px"></div>
  <div class="rule" style="left:32px;top:351px;width:285px"></div>
  <div class="rule" style="left:32px;top:374px;width:285px"></div>
  <div class="rule" style="left:32px;top:397px;width:285px"></div>
  <div class="rule" style="left:32px;top:420px;width:285px"></div>

  <div class="rule" style="left:351px;top:260px;width:320px"></div>
  <div class="rule" style="left:351px;top:283px;width:320px"></div>
  <div class="rule" style="left:351px;top:306px;width:320px"></div>
  <div class="rule" style="left:351px;top:329px;width:320px"></div>
  <div class="rule" style="left:351px;top:351px;width:320px"></div>
  <div class="rule" style="left:351px;top:374px;width:320px"></div>
  <div class="rule" style="left:351px;top:397px;width:320px"></div>
  <div class="rule" style="left:351px;top:420px;width:320px"></div>
  <div class="rule" style="left:351px;top:443px;width:320px"></div>
</section>

</body>
</html>
```